Quillstone Restaurnt Lunch Menu Redesign:

We have two lunch special menus that need to be reformatted into a 4.25inx11in and need a graphics design update. Some menu items need to change and some descriptions need to updated. This new menu should double sided with the Main Dining Lunch Menu on the front side and Teppanyaki Lunch menu on the back.

Both menus should follow the same design formatting as the main dining lunch menu (font, sizing, ect.)

```html
<!DOCTYPE html>
<html lang="en">
<head>
<meta charset="utf-8">
<title>Quillstone Lunch Specials</title>
<link rel="stylesheet" href="https://fonts.googleapis.com/css2?family=Abril+Fatface&family=Kaushan+Script&family=Open+Sans:ital,wght@0,400;0,600;1,400&display=swap">
<style>
:root{
  --navy:#0b2e8a;
  --ink:#222;
  --price:#5a5a5a;
  --muted:#444;
  --shade:#f4f4f4;
  --rule:#d6d6d6;
  --gold:#c8a96a;
  --page:#ffffff;
  --backdrop:#f7f7f7;
}
*{box-sizing:border-box;margin:0;padding:0}
html,body{width:932px;height:1200px;overflow:hidden}
body{background:var(--backdrop);font-family:"Open Sans",Arial,sans-serif;color:var(--ink);position:relative}
.menu-page{position:absolute;top:130px;width:400px;height:1034px;background:var(--page);box-shadow:0 0 40px rgba(0,0,0,.06)}
.menu-page--main{left:45px}
.menu-page--teppanyaki{left:487px}
.brand{position:absolute;top:26px;left:0;right:0;text-align:center;font-size:15px;font-weight:600;color:var(--navy);letter-spacing:.5px}
.page-title{position:absolute;top:54px;left:0;right:0;text-align:center;font-family:"Abril Fatface",Georgia,serif;font-size:29px;font-weight:400;color:var(--navy)}
.hours{position:absolute;top:96px;left:0;right:0;display:flex;justify-content:center;align-items:center;gap:6px;font-size:8.5px;font-weight:600;color:var(--navy)}
.hours::before,.hours::after{content:"";width:26px;height:1px;background:var(--navy)}
.hours span{background:var(--shade);padding:1px 5px;border-radius:3px}
.section{position:absolute;left:0;right:0}
.banner{position:relative;width:160px;height:33px;margin:0 auto}
.banner svg{position:absolute;inset:0}
.banner h2{position:relative;text-align:center;font-family:"Kaushan Script",cursive;font-weight:400;color:#fff;font-size:18px;line-height:33px}
.section-note{width:196px;margin:5px auto 0;padding-bottom:4px;border-bottom:1px solid var(--rule);text-align:center;font-size:6.8px;line-height:8.4px;color:var(--muted)}
.section-note--wide{width:210px}
.items{list-style:none;margin:6px 38px 0 38px}
.item{display:flex;justify-content:space-between;align-items:center;padding:0 8px 0 2px;font-size:12px;line-height:14px}
.item:nth-child(even){background:var(--shade)}
.item--tall{height:37px}
.item--single{height:26px}
.item-desc{display:block;font-style:italic;font-size:9.5px;line-height:11.5px;color:var(--ink)}
.item-desc--inline{display:inline}
.price{color:var(--price);font-size:12px;white-space:nowrap}
.sushi-grid{position:relative;margin:6px 38px 0;height:180px}
.sushi-col{list-style:none;position:absolute}
.sushi-col li{height:26px;line-height:26px;font-size:12px;padding-left:1px}
.sushi-col li i{font-size:9.5px}
.sushi-col--left{left:0;width:138px}
.sushi-col--left li:nth-child(even),.sushi-col--top li:nth-child(even){background:var(--shade)}
.sushi-col--top{left:184px;width:138px}
.sushi-col--accent{left:184px;top:70px;border-left:1.5px solid var(--gold);padding-left:6px;width:138px}
.legal{position:absolute;top:996px;left:0;right:0;text-align:center;font-size:8.2px;line-height:10.5px;font-style:italic;color:var(--ink)}
.legal b{font-style:normal;font-weight:600}
</style>
</head>
<body>

<section class="menu-page menu-page--main">
  <div class="brand">Quillstone</div>
  <h1 class="page-title">Lunch Specials</h1>
  <p class="hours"><span>Served Daily 11AM - 3PM</span></p>

  <div class="section" style="top:132px">
    <div class="banner"><svg viewBox="0 0 160 33" preserveAspectRatio="none"><path d="M0 6 Q80 -5 160 6 L160 33 Q80 24 0 33 Z" fill="var(--navy)"/></svg><h2>Sandwiches</h2></div>
    <p class="section-note section-note--wide">Served with Choice of Miso Soup or House Salad &amp; Potato Chips</p>
    <ul class="items">
      <li class="item item--tall"><span>Fried Breaded Calamari Steak<span class="item-desc">with Tomato, Lettuce &amp; Onion</span></span><span class="price">$ 16</span></li>
      <li class="item item--tall"><span>Grilled Chicken <span class="item-desc item-desc--inline">with Bacon, Tomato,</span><span class="item-desc">Lettuce &amp; Mayonnaise Drizzle</span></span><span class="price">$ 16</span></li>
      <li class="item item--tall"><span>Hamburger <span class="item-desc item-desc--inline">with Lettuce, Tomato,</span><span class="item-desc">Onion, Mayonnaise Drizzle</span></span><span class="price">$ 18</span></li>
      <li class="item item--tall"><span>Fried Soft Shell Crab Burger<span class="item-desc">with Avocado, Lettuce, Tomato, Onion &amp; Mayo</span></span><span class="price">$ 20</span></li>
    </ul>
  </div>

  <div class="section" style="top:365px">
    <div class="banner"><svg viewBox="0 0 160 33" preserveAspectRatio="none"><path d="M0 6 Q80 -5 160 6 L160 33 Q80 24 0 33 Z" fill="var(--navy)"/></svg><h2>Sushi Specials</h2></div>
    <p class="section-note section-note--wide">Please Select 4 of the followings for $16<br>Served with a 4 piece California Roll &amp; Miso Soup or House Salad</p>
    <div class="sushi-grid">
      <ul class="sushi-col sushi-col--left">
        <li>Hamachi <i>Yellowtail Tuna</i></li>
        <li>Hotate <i>Yellowtail</i></li>
        <li>Ika <i>Squid</i></li>
        <li>Ikura <i>Salmon Roe</i></li>
        <li>Saba <i>Mackerel</i></li>
        <li>Sake <i>Salmon</i></li>
        <li>Tai <i>Red Snapper</i></li>
      </ul>
      <ul class="sushi-col sushi-col--top">
        <li>Maguro <i>Yellowtail Tuna</i></li>
        <li>Smoked Salmon</li>
      </ul>
      <ul class="sushi-col sushi-col--accent">
        <li>Tako <i>Octopus</i></li>
        <li>Unagi <i>BBQ Eel</i></li>
        <li>Ebi <i>Shrimp</i></li>
        <li>Tamago <i>Egg</i></li>
      </ul>
    </div>
  </div>

  <div class="section" style="top:633px">
    <div class="banner"><svg viewBox="0 0 160 33" preserveAspectRatio="none"><path d="M0 6 Q80 -5 160 6 L160 33 Q80 24 0 33 Z" fill="var(--navy)"/></svg><h2>Main Courses</h2></div>
    <p class="section-note">Served with Rice &amp; Choice of Miso Soup or House Salad<br>All Meals Served with Rice. Upgrade to fried rice for only $4</p>
    <ul class="items">
      <li class="item item--tall"><span>Organic Tofu Teriyaki<span class="item-desc">Served Grilled or Tempura Fried</span></span><span class="price">$ 14</span></li>
      <li class="item item--single"><span>Chicken Teriyaki</span><span class="price">$ 16</span></li>
      <li class="item item--single"><span>Spicy Chicken Teriyaki</span><span class="price">$ 16</span></li>
      <li class="item item--single"><span>Beef Teriyaki</span><span class="price">$ 16</span></li>
      <li class="item item--single"><span>Spicy Beef Teriyaki</span><span class="price">$ 16</span></li>
      <li class="item item--tall"><span>Chicken Kats<span class="item-desc">Breaded Chicken Breast</span></span><span class="price">$ 15</span></li>
      <li class="item item--tall"><span>Katsu Don<span class="item-desc">Fried Chicken Breast, Egg &amp; Onion over Rice</span></span><span class="price">$ 16</span></li>
      <li class="item item--tall"><span>Unagi Don<span class="item-desc">BBQ Eel over Rice</span></span><span class="price">$ 19</span></li>
      <li class="item item--single"><span>Shrimp &amp; Vegetable Tempura</span><span class="price">$ 16</span></li>
    </ul>
  </div>

  <p class="legal"><b>Served Raw:</b> 20% gratuity added to parties of 6 or more.<br>Consuming raw or undercooked food may increase your risk of foodborne illness</p>
</section>

<section class="menu-page menu-page--teppanyaki">
  <div class="brand">Quillstone</div>
  <h1 class="page-title">Lunch Specials</h1>
  <p class="hours"><span>Served Daily 11AM - 3PM</span></p>

  <div class="section" style="top:152px">
    <div class="banner"><svg viewBox="0 0 160 33" preserveAspectRatio="none"><path d="M0 6 Q80 -5 160 6 L160 33 Q80 24 0 33 Z" fill="var(--navy)"/></svg><h2>Teppanyaki Lunch</h2></div>
    <p class="section-note section-note--wide">Served with Miso Soup or Salad, Choice of Rice &amp; Vegetables</p>
    <ul class="items">
      <li class="item item--single"><span>Hibachi Chicken</span><span class="price">$ 18</span></li>
      <li class="item item--single"><span>Hibachi Shrimp</span><span class="price">$ 19</span></li>
      <li class="item item--single"><span>Hibachi New York Steak</span><span class="price">$ 20</span></li>
      <li class="item item--single"><span>Hibachi Salmon</span><span class="price">$ 20</span></li>
      <li class="item item--single"><span>Teriyaki Beef</span><span class="price">$ 19</span></li>
      <li class="item item--single"><span>Hibachi Scallop</span><span class="price">$ 20</span></li>
      <li class="item item--single"><span>Chicken and Shrimp</span><span class="price">$ 21</span></li>
      <li class="item item--single"><span>Scallop and Shrimp</span><span class="price">$ 22</span></li>
      <li class="item item--single"><span>New York Steak and Chicken</span><span class="price">$ 22</span></li>
      <li class="item item--single"><span>New York Steak and Shrimp</span><span class="price">$ 23</span></li>
      <li class="item item--single"><span>New York Steak and Scallop</span><span class="price">$ 24</span></li>
      <li class="item item--single"><span>Filet Mignon</span><span class="price">$ 23</span></li>
      <li class="item item--single"><span>Filet Mignon and Chicken</span><span class="price">$ 25</span></li>
      <li class="item item--single"><span>Filet Mignon and Shrimp</span><span class="price">$ 26</span></li>
      <li class="item item--single"><span>Filet Mignon and Scallop</span><span class="price">$ 27</span></li>
    </ul>
  </div>

  <div class="section" style="top:626px">
    <div class="banner"><svg viewBox="0 0 160 33" preserveAspectRatio="none"><path d="M0 6 Q80 -5 160 6 L160 33 Q80 24 0 33 Z" fill="var(--navy)"/></svg><h2>Special Menu</h2></div>
    <p class="section-note section-note--wide">Ages 12 and Under ~ Ages 65 and Older<br>Served with Miso Soup or Salad, Choice of Rice &amp; Vegetables</p>
    <ul class="items">
      <li class="item item--single"><span>Hibachi Chicken</span><span class="price">$ 15</span></li>
      <li class="item item--single"><span>Hibachi Shrimp</span><span class="price">$ 16</span></li>
      <li class="item item--single"><span>Hibachi New York Steak</span><span class="price">$ 18</span></li>
      <li class="item item--single"><span>Hibachi Scallop</span><span class="price">$ 18</span></li>
      <li class="item item--single"><span>Teriyaki Beef</span><span class="price">$ 16</span></li>
    </ul>
  </div>
</section>

</body>
</html>
```